KESTREL REFRIGERATION Business Card design

We are looking for a business card design front and back. We would like our logo only on the front with all other details on the rear.
Rear should include name, email address and two phone numbers. Similar to the attachment.
Smart and bright.
Looking for a matt finish on all of the card but the logo to be gloss and slightly proud.

Contact Information for Business Card

Name - Gavin Holloway
Director
Phone - 0867302948
0417259083
email - gavin@kestrelrefrigeration.com.au
website - kestrelrefrigeration.com.au

Font styles to use
Serif

Requirements
Must have
• Colours from our logo. icons for phone, email etc.

```html
<!DOCTYPE html>
<html lang="en">
<head>
<meta charset="utf-8">
<title>Kestrel Refrigeration – Business Card</title>
<link href="https://fonts.googleapis.com/css2?family=Teko:wght@500;600&family=PT+Sans:wght@400&display=swap" rel="stylesheet">
<style>
  :root {
    --backdrop: #dcdcd9;
    --paper: #ffffff;
    --lime: #a4f06a;
    --plum: #3f2a5e;
    --plum-card: #432b62;
    --lavender: #e2dbee;
    --ink-grey: #555459;
    --rule: #c9c6cf;
  }
  * { margin: 0; padding: 0; box-sizing: border-box; }
  html, body {
    width: 1146px;
    height: 1200px;
    overflow: hidden;
    background: var(--backdrop);
  }
  .card {
    position: absolute;
    left: 207px;
    width: 729px;
    height: 422px;
    overflow: hidden;
  }
  .card--front { top: 125px; background: var(--paper); }
  .card--back  { top: 655px; height: 417px; background: var(--plum-card); }

  .brand {
    position: absolute;
    text-align: center;
    font-family: "Teko", sans-serif;
    line-height: 1;
  }
  .brand__name {
    display: block;
    font-weight: 600;
    color: var(--lime);
    letter-spacing: 0.5px;
    white-space: nowrap;
  }
  .brand__tag {
    display: block;
    font-weight: 500;
    letter-spacing: 0.5px;
    white-space: nowrap;
  }
  .card--front .brand { left: 60px; top: 175px; width: 272px; }
  .card--front .brand__name { font-size: 84px; height: 84px; }
  .card--front .brand__tag { font-size: 28px; color: var(--plum); margin-top: 0; }

  .card--back .brand { left: 0; top: 136px; width: 100%; }
  .card--back .brand__name { font-size: 112px; height: 112px; }
  .card--back .brand__tag { font-size: 36px; color: var(--lavender); margin-top: 16px; }

  .divider {
    position: absolute;
    left: 342px;
    top: 136px;
    width: 1px;
    height: 154px;
    background: var(--rule);
  }
  .person {
    position: absolute;
    left: 373px;
    top: 134px;
    font-family: "Teko", sans-serif;
    line-height: 1;
  }
  .person__name {
    font-size: 44px;
    font-weight: 500;
    color: var(--plum);
    letter-spacing: 0.3px;
  }
  .person__role {
    font-size: 27px;
    font-weight: 500;
    color: var(--lime);
    margin-top: -6px;
  }
  .contact {
    position: absolute;
    left: 373px;
    top: 212px;
    list-style: none;
    font-family: "PT Sans", sans-serif;
    font-size: 17px;
    color: var(--ink-grey);
  }
  .contact__item {
    display: flex;
    align-items: center;
    height: 23.5px;
  }
  .contact__icon {
    width: 16px;
    height: 16px;
    margin-right: 11px;
    fill: var(--plum);
    flex: none;
  }
</style>
</head>
<body>
  <section class="card card--front">
    <div class="brand">
      <span class="brand__name">KESTREL</span>
      <span class="brand__tag">REFRIGERATION</span>
    </div>
    <div class="divider"></div>
    <div class="person">
      <div class="person__name">GAVIN HOLLOWAY</div>
      <div class="person__role">DIRECTOR</div>
    </div>
    <ul class="contact">
      <li class="contact__item">
        <svg class="contact__icon" viewBox="0 0 16 16" aria-hidden="true"><path d="M3.6 1.2l2.3 2.6c.3.4.3.9 0 1.3L4.7 6.4c.9 2 2.6 3.8 4.7 4.8l1.3-1.2c.4-.3.9-.3 1.3 0l2.6 2.2c.4.4.4.9.1 1.3l-1.3 1.5c-.4.4-1 .6-1.6.4C6.4 14 2.1 9.7.6 4.2.4 3.6.6 3 1 2.6L2.3 1.2c.4-.4 1-.4 1.3 0z"/></svg>
        <span>0867302948 / 0417259083</span>
      </li>
      <li class="contact__item">
        <svg class="contact__icon" viewBox="0 0 16 16" aria-hidden="true"><path d="M0 3h16v10H0z M1.5 4.2v.4L8 9l6.5-4.4v-.4z" fill-rule="evenodd"/></svg>
        <span>gavin@kestrelrefrigeration.com.au</span>
      </li>
      <li class="contact__item">
        <svg class="contact__icon" viewBox="0 0 16 16" aria-hidden="true"><circle cx="8" cy="8" r="7.5"/><path d="M5 3.5c1.5.3 2 1.3 1.4 2.3-.5.8.4 1.5 1.3 1.6 1 .1 1 1.3.3 2-.6.7-.3 1.9.4 2.6-2 .3-3.7-.6-4.6-2.1.8-.5 1.1-1.5.6-2.3C4 7 3.6 6.3 3.2 5.8 3.7 4.8 4.3 4 5 3.5zM10.5 3c1 .4 1.7 1 2.3 1.9-.8.3-1.7 0-2.1-.5-.3-.5-.4-1-.2-1.4z" fill="#ffffff"/></svg>
        <span>kestrelrefrigeration.com.au</span>
      </li>
    </ul>
  </section>

  <section class="card card--back">
    <div class="brand">
      <span class="brand__name">KESTREL</span>
      <span class="brand__tag">REFRIGERATION</span>
    </div>
  </section>
</body>
</html>
```